Creative - Appealing - Business Card Design Project

Looking for a Business card design (vector artwork) for an existing company called 'Fernway Sound'. We operate in the entertainment industry specializing in audio system design and rental, however; we also deal with other sectors of the entertainment industry including lighting, video, staging and power system design and rental. We would like to see designs that don't focus too much on audio but include elements encompassing everything else.

Double sided business card, following our new colour scheme and logo, which is attached. The card would ideally be creative and eye catching to draw in new customers in the elegant event production market, such as weddings & corporate affairs.

Target Market(s)

High end corporate clients, wedding clients

Industry/Entity Type

Entertainment

Requirements
Must have
• Our contact details, these can be worded & listed however you think appropriate as part as the design

Business Name - Fernway Sound
My Name - Dominic Harwell
Web Address - www.fernwaysound-example.com
Mobile Number - 07914 362 517
Office Number - 0330 481 7265
Email - dom@fernwaysound-example.com

The name, email and mobile number would need to be able to be changed to my business partners also.

The font used on our logo is Sansation
Nice to have
• On one side maybe a word cloud involving the services in which we can provide; Lighting, Sound, Event Production, Staging, LED Uplighting, Projection Mapping, Wedding Hire

On the other side, all the important credentials of contact.
Should not have
• The design should not use any old style fonts (i.e Times New Roman, Gothic etc) or on the other side of the scale, any 'jokey' fonts (i.e. Comic Sans).

The font to be used is Sansation

```html
<!DOCTYPE html>
<html lang="en">
<head>
<meta charset="utf-8">
<title>Fernway Sound – Business Card</title>
<link rel="stylesheet" href="https://fonts.googleapis.com/css2?family=Sansation:wght@400;700&display=swap">
<style>
  :root {
    --purple: #5a2f83;
    --purple-deep: #472570;
    --purple-soft: #7d55a3;
    --purple-light: #8a62b0;
    --ink: #1f1f24;
    --grey: #8c8c8f;
    --card: #ffffff;
    --backdrop: #e6e6e8;
  }
  * { box-sizing: border-box; margin: 0; padding: 0; }
  html, body { width: 1200px; height: 900px; overflow: hidden; }
  body {
    background: var(--backdrop);
    font-family: "Sansation", "Helvetica Neue", Arial, sans-serif;
    position: relative;
  }
  .card {
    position: absolute;
    top: 307px;
    width: 513px;
    height: 285px;
    background: var(--card);
    box-shadow: 0 2px 6px rgba(0,0,0,0.18);
    overflow: hidden;
  }
  .card--front { left: 73px; }
  .card--back  { left: 615px; }

  /* Front */
  .front-block {
    position: absolute;
    left: 0;
    top: 0;
    width: 230px;
    height: 230px;
    background: linear-gradient(160deg, var(--purple-light) 0%, var(--purple) 55%, var(--purple-deep) 100%);
  }
  .front-name {
    position: absolute;
    left: 250px;
    top: 34px;
    font-size: 30px;
    font-weight: 700;
    color: var(--purple);
    white-space: nowrap;
  }
  .front-footer {
    position: absolute;
    right: 28px;
    bottom: 26px;
    text-align: right;
  }
  .front-url {
    font-size: 16px;
    color: var(--purple);
    margin-bottom: 3px;
    white-space: nowrap;
  }
  .services {
    font-size: 9.5px;
    line-height: 11.5px;
    color: var(--grey);
    white-space: nowrap;
  }

  /* Back */
  .back-brand {
    position: absolute;
    left: 20px;
    top: 0;
    width: 185px;
    height: 100%;
    display: flex;
    flex-direction: column;
    align-items: center;
    justify-content: center;
    gap: 14px;
  }
  .brand-square {
    width: 56px;
    height: 56px;
    background: var(--purple);
  }
  .back-brand .brand-name {
    font-size: 24px;
    font-weight: 700;
    color: var(--grey);
    white-space: nowrap;
  }
  .divider {
    position: absolute;
    left: 222px;
    top: 43px;
    width: 1.5px;
    height: 207px;
    background: var(--purple-soft);
  }
  .contact {
    position: absolute;
    left: 245px;
    top: 66px;
    color: var(--ink);
    white-space: nowrap;
  }
  .contact-name {
    font-size: 16.5px;
    font-weight: 700;
    color: var(--purple);
  }
  .contact-role {
    font-size: 14.5px;
    margin-top: 1px;
  }
  .contact-company {
    font-size: 16.5px;
    color: var(--purple);
    margin-top: 28px;
  }
  .contact-list { list-style: none; margin-top: 1px; }
  .contact-list li {
    display: flex;
    align-items: center;
    gap: 7px;
    font-size: 13px;
    line-height: 16.5px;
  }
  .contact-list svg { width: 10px; height: 10px; flex: none; fill: var(--purple-deep); }
</style>
</head>
<body>

  <section class="card card--front" aria-label="Card front">
    <div class="front-block" aria-hidden="true"></div>
    <p class="front-name">Fernway Sound</p>
    <div class="front-footer">
      <p class="front-url">www.fernwaysound-example.com</p>
      <p class="services">Lighting • Sound • Event Production • Staging<br>LED Uplighting • Projection Mapping • Wedding Hire</p>
    </div>
  </section>

  <section class="card card--back" aria-label="Card back">
    <div class="back-brand">
      <span class="brand-square" aria-hidden="true"></span>
      <span class="brand-name">Fernway Sound</span>
    </div>
    <div class="divider"></div>
    <div class="contact">
      <p class="contact-name">Dominic Harwell</p>
      <p class="contact-role">managing director</p>
      <p class="contact-company">Fernway Sound</p>
      <ul class="contact-list">
        <li>
          <svg viewBox="0 0 10 10" aria-hidden="true"><path d="M3 0h4a1 1 0 0 1 1 1v8a1 1 0 0 1-1 1H3a1 1 0 0 1-1-1V1a1 1 0 0 1 1-1zm0 1.5v6h4v-6z"/></svg>
          07914 362 517
        </li>
        <li>
          <svg viewBox="0 0 10 10" aria-hidden="true"><path d="M2.2 0.5l1.6 2-0.9 1.2c.6 1.3 1.6 2.3 2.9 2.9l1.2-.9 2 1.6-1 1.8C4.6 9 1 5.4 0.9 1.5z"/></svg>
          0330 481 7265
        </li>
        <li>
          <svg viewBox="0 0 10 10" aria-hidden="true"><path d="M0 2h10v6H0zM0.8 2.6L5 5.6l4.2-3z" fill-rule="evenodd"/></svg>
          dom@fernwaysound-example.com
        </li>
        <li>
          <svg viewBox="0 0 10 10" aria-hidden="true"><path d="M5 0a5 5 0 1 0 0 10A5 5 0 0 0 5 0zm0 1c.6.7 1 1.8 1.1 3.5H3.9C4 2.8 4.4 1.7 5 1zM1.1 4.5A4 4 0 0 1 3.2 1.4C3 2.3 2.9 3.3 2.9 4.5zm0 1h1.8c0 1.2.1 2.2.3 3.1A4 4 0 0 1 1.1 5.5zm2.8 0h2.2C6 7.2 5.6 8.3 5 9c-.6-.7-1-1.8-1.1-3.5zm3.2 0h1.8a4 4 0 0 1-2.1 3.1c.2-.9.3-1.9.3-3.1zm0-1c0-1.2-.1-2.2-.3-3.1a4 4 0 0 1 2.1 3.1z"/></svg>
          www.fernwaysound-example.com
        </li>
      </ul>
    </div>
  </section>

</body>
</html>
```